KestavLaw a fully remote and fully bilingual law firm for the Florida injured

1. Can you describe what your company does?- a solo lawyer practice in Florida, D.C., and soon in NY. I offer services for auto accidents, negligence, boat accident, motorcycle accident, insurance claims, premises liability, and things of the like.

2. Who are your target customers for the website? Drivers, passengers, pedestrians involved in accidents where they were injured and need help making a claim against the other vehicle or insurance company- throughout the entire state of Florida, but primarily in greater central florida area for english speaking and latino community offering a 100% bilingual services ENGLISH/SPANISH and 100% remote, where I wont make clients come to an office ever, and will private online meetings, signing portals, and all to have it efficient for clients benefit.

3. Do you have an existing domain name / website address? yes, kestavlaw.example through Bramblefield Suite. i need help in getting in brought to you so you can handle it please.

4. In addition to a Home Page, which other pages / sections would you like your website to have:
About Us
Contact Us
Products / Services
Office / Mailing Address
Testimonials / Reviews
FAQs
Terms and Conditions
Any other page / section you would like- DO EVERYTHING IN BOTH LANGUAGES- ENGLISH AND SPANISH
I want the page to have a way for people to calendar appts with me. and also
to make transactions - accepting all methods of payment

For each of the pages / sections you’d like to have, please provide the text (and images, if available) you would like to include.

5. Which of the below are features and functionalities your website will need:
Image Gallery
Videos
Contact Form
Mailing List
Maps
FAQs
Accepting payments / donations
6. Please provide the URLs for the social media profiles you'd like to link to the website. I have none, I am just starting, I actually want to have the online presence ready before my official launch.

Target Market(s)

Injured individuals by the negligent act of another in Florida

Industry/Entity Type

LAWYER/ AUTO ACCIDENT/NEGLIGENCE/ PREMISES LIABILITY/ CIVIL LAW

Coding

Coded - Design and coding required

Number of Pages Required

1 page

Requirements
Must have
• bilingual ENGLISH and SPANISH; a button for people to calendar appointments with me; accept payments, and to be able to integrate with major software like quillseal, pinnex, etc since I need to integrate under the fully remote platform
Nice to have
• look at my logo from markforge.example it has the Dellacorte Law and KestavLaw.example together.. I have the kestavlaw.example domain from Bramblefield. need you guys to help integrate that too , meaning to be able to use that domain for my website.

```html
<!DOCTYPE html>
<html lang="en">
<head>
<meta charset="utf-8">
<title>Blog | Dellacorte Law</title>
<link href="https://fonts.googleapis.com/css2?family=Poppins:ital,wght@0,400;0,500;0,600;1,400&family=Oswald:wght@500;600&family=Cinzel:wght@500&display=swap" rel="stylesheet">
<style>
:root{
  --navy:#1f2f5c;
  --navy-deep:#17224a;
  --gold:#c9a03b;
  --gold-soft:#d4ac45;
  --ink:#222630;
  --muted:#6e6e6e;
  --line:#dcdcdc;
  --band:#f3f3f3;
  --white:#ffffff;
  --black:#050505;
}
*{box-sizing:border-box;margin:0;padding:0}
html,body{width:1200px;height:3178px;overflow:hidden;background:var(--white)}
body{font-family:'Poppins',sans-serif;color:var(--ink);position:relative}
a{text-decoration:none;color:inherit}
.page{position:relative;width:1200px;height:3178px;overflow:hidden}

/* hero */
.hero{position:absolute;left:0;top:0;width:1200px;height:557px;background:var(--band)}
.hero-art{position:absolute;left:0;top:0}
.site-header{position:absolute;left:0;top:0;width:1200px;height:110px}
.brand{position:absolute;left:22px;top:14px;width:140px;text-align:center;color:var(--white)}
.brand-mark{width:58px;height:58px;border:2px solid var(--white);border-radius:50%;margin:0 auto 8px}
.brand-name{font-family:'Oswald',sans-serif;font-weight:500;font-size:15px;letter-spacing:3.4px;white-space:nowrap}
.main-nav{position:absolute;left:219px;top:32px;display:flex;gap:0;font-size:13.5px;color:var(--white)}
.main-nav a{position:absolute;white-space:nowrap}
.main-nav .active{color:var(--gold-soft)}
.lang{position:absolute;left:740px;top:27px;width:82px;height:28px;border:1px solid var(--white);border-radius:14px;color:var(--white);font-size:12px;display:flex;align-items:center;justify-content:center;gap:6px}
.lang-dot{width:20px;height:12px;background:#c9d3e6;border-radius:2px}
.divider-v{position:absolute;left:836px;top:26px;height:32px;border-left:1px dashed rgba(255,255,255,.6)}
.btn-pay{position:absolute;left:852px;top:22px;width:151px;height:38px;border-radius:19px;background:var(--gold);color:var(--white);font-size:13.5px;display:flex;align-items:center;justify-content:center}
.call{position:absolute;left:1015px;top:22px;color:var(--white);display:flex;align-items:center;gap:10px}
.call-icon{width:36px;height:36px;border-radius:50%;background:var(--gold);display:flex;align-items:center;justify-content:center}
.call small{display:block;font-size:13px;line-height:16px}
.call strong{display:block;font-size:17px;font-weight:600;line-height:22px}
.hero-copy{position:absolute;left:142px;top:166px;width:380px;color:var(--white)}
.hero-title{font-family:'Cinzel',serif;font-weight:500;font-size:42px;line-height:52px;padding-left:14px;border-left:3px solid var(--gold);margin-bottom:20px}
.hero-text{font-size:13.5px;line-height:22.5px}
.btn-consult{position:absolute;left:142px;top:348px;width:254px;height:44px;border-radius:22px;background:var(--gold);color:var(--white);font-size:13.5px;display:flex;align-items:center;justify-content:center;gap:10px}
.scroll-down{position:absolute;left:578px;top:485px;width:40px;height:40px;border-radius:50%;background:var(--white);box-shadow:0 2px 8px rgba(0,0,0,.18);display:flex;align-items:center;justify-content:center}
.breadcrumb{position:absolute;left:141px;top:527px;font-size:13px;color:#7d8bab;display:flex;gap:10px;align-items:center}
.breadcrumb .current{color:var(--navy)}

/* section heading */
.section-title{position:absolute;left:0;top:634px;width:1200px;text-align:center;font-family:'Oswald',sans-serif;font-weight:600;font-size:35px;letter-spacing:3px;color:var(--navy)}
.section-rule{position:absolute;left:575px;top:691px;width:50px;height:2px;background:var(--gold)}

/* posts */
.post-grid{position:absolute;left:141px;top:721px;display:grid;grid-template-columns:286px 286px;grid-auto-rows:446px;column-gap:28px;row-gap:28px}
.post-card{border:1px solid var(--line);background:var(--white);display:flex;flex-direction:column}
.post-media{height:169px;width:100%}
.post-body{padding:18px 16px 0;font-size:13px;line-height:23px}
.post-meta span{color:var(--gold)}
.post-meta em{font-style:italic}
.post-title{font-size:14.5px;font-weight:500;line-height:24px;margin:9px 0 4px;color:var(--ink)}
.post-excerpt{color:var(--muted);font-size:13.2px;line-height:22.5px}
.post-actions{display:flex;align-items:center;margin-top:20px;font-size:13px;color:var(--navy);font-weight:500}
.post-actions a{display:flex;align-items:center;gap:7px}
.post-actions .sep{width:1px;height:18px;background:var(--line);margin:0 14px}

/* sidebar */
.sidebar{position:absolute;left:769px;top:721px;width:290px}
.widget{border:1px solid var(--line);background:var(--white);margin-bottom:30px}
.widget-search{padding:18px 16px 16px;height:111px}
.widget-search h3{font-size:16.5px;font-weight:500;margin-bottom:10px}
.search-field{height:41px;background:#f1f1f1;display:flex;align-items:center;gap:12px;padding:0 12px;font-size:13px;color:#8a8a8a}
.widget-head{height:50px;background:var(--gold);color:var(--white);font-size:17px;font-weight:500;display:flex;align-items:center;padding-left:16px}
.cat-list{list-style:none;padding:0 16px}
.cat-list li{height:59px;display:flex;align-items:center;gap:14px;font-size:14.5px;border-bottom:1px solid var(--line)}
.cat-list li:last-child{border-bottom:none}
.recent-list{list-style:none;padding:0 16px}
.recent-list li{height:107px;display:flex;align-items:center;gap:16px;border-bottom:1px solid var(--line)}
.recent-list li:last-child{border-bottom:none}
.recent-thumb{width:71px;height:71px;flex:none}
.recent-list h4{font-size:14.5px;font-weight:500;margin-bottom:6px}
.recent-date{font-size:13px;display:flex;align-items:center;gap:10px}

/* pagination */
.pagination{position:absolute;left:275px;top:2618px;height:28px;display:flex;align-items:center;font-size:14.5px;color:var(--muted)}
.pagination .page-num{position:absolute;top:0;height:28px;display:flex;align-items:center;justify-content:center;white-space:nowrap}
.pagination .is-current{background:var(--gold);color:var(--white);width:28px}

/* footer */
.site-footer{position:absolute;left:0;top:2700px;width:1200px;height:478px;background:var(--black);color:var(--white)}
.footer-curve{position:absolute;left:0;top:0}
.footer-brand{position:absolute;left:60px;top:166px;width:260px;text-align:center}
.footer-brand .brand-mark{width:80px;height:80px;margin-bottom:12px}
.footer-brand .brand-name{font-size:22px;letter-spacing:5.5px}
.socials{position:absolute;left:110px;top:316px;display:flex;gap:8px}
.socials a{width:32px;height:32px;border-radius:50%;border:1px solid var(--white);font-size:8.5px;display:flex;align-items:center;justify-content:center}
.socials a.on{background:var(--navy);border-color:var(--navy)}
.footer-col{position:absolute;top:168px}
.footer-col h5{font-family:'Oswald',sans-serif;font-weight:500;font-size:17px;letter-spacing:2px;margin-bottom:6px}
.footer-col .rule{width:34px;height:2px;background:var(--gold);margin-bottom:14px}
.footer-col ul{list-style:none;font-size:13.2px;line-height:27.5px}
.contact-list{list-style:none;font-size:13.2px;line-height:20px}
.contact-list li{display:flex;gap:10px;margin-bottom:16px}
.contact-list svg{flex:none;margin-top:3px}
.footer-bottom{position:absolute;left:70px;top:414px;width:1060px;border-top:1px solid #333}
.copyright{position:absolute;left:70px;top:438px;font-size:13px}
.copyright strong{font-weight:500}
.pay-methods{position:absolute;left:903px;top:433px;display:flex;gap:4px}
.pay-methods span{width:42px;height:28px;background:var(--white);color:var(--navy);border-radius:3px;font-size:8.5px;font-weight:500;display:flex;align-items:center;justify-content:center}
</style>
</head>
<body>
<div class="page">

  <section class="hero">
    <svg class="hero-art" width="1200" height="560" viewBox="0 0 1200 560">
      <defs>
        <linearGradient id="heroTone" x1="0" y1="0" x2="1" y2="0.4">
          <stop offset="0" stop-color="#1d2b58"/>
          <stop offset="0.45" stop-color="#31406a"/>
          <stop offset="0.75" stop-color="#6c6a68"/>
          <stop offset="1" stop-color="#8c6a3e"/>
        </linearGradient>
      </defs>
      <path role="img" aria-label="Lawyer and client reviewing and signing a contract at a desk" d="M0 0 H1200 V445 Q600 555 0 445 Z" fill="url(#heroTone)"/>
      <path d="M0 455 Q600 565 1200 455" fill="none" stroke="#c9a03b" stroke-width="3"/>
    </svg>

    <header class="site-header">
      <a class="brand" href="#">
        <div class="brand-mark"></div>
        <div class="brand-name">DELLACORTE LAW</div>
      </a>
      <nav class="main-nav">
        <a href="#" style="left:0">Home</a>
        <a href="#" style="left:61px">About Us</a>
        <a href="#" style="left:142px">Services</a>
        <a href="#" style="left:219px">Testimonials</a>
        <a href="#" style="left:318px">FAQ’s</a>
        <a href="#" class="active" style="left:376px">Blog</a>
        <a href="#" style="left:428px">Contact Us</a>
      </nav>
      <div class="lang"><span class="lang-dot"></span>EN
        <svg width="8" height="6" viewBox="0 0 8 6"><path d="M1 1l3 3 3-3" stroke="#fff" fill="none" stroke-width="1.3"/></svg>
      </div>
      <div class="divider-v"></div>
      <a class="btn-pay" href="#">Make a Payment</a>
      <div class="call">
        <span class="call-icon"><svg width="18" height="18" viewBox="0 0 24 24"><path fill="#fff" d="M6.6 10.8a15.1 15.1 0 006.6 6.6l2.2-2.2a1 1 0 011-.25 11.4 11.4 0 003.6.57 1 1 0 011 1V20a1 1 0 01-1 1A17 17 0 013 4a1 1 0 011-1h3.5a1 1 0 011 1c0 1.25.2 2.45.57 3.57a1 1 0 01-.25 1z"/></svg></span>
        <div><small>Call Us Today</small><strong>123 456 7890</strong></div>
      </div>
    </header>

    <div class="hero-copy">
      <h1 class="hero-title">BLOG</h1>
      <p class="hero-text">Bilingual legal services for auto accidents, negligence claims, and personal injury cases throughout Florida, DC, and soon NY. 100% remote consultations available.</p>
    </div>
    <a class="btn-consult" href="#">Schedule Free Consultation
      <svg width="22" height="12" viewBox="0 0 22 12"><path d="M0 6h20M15 1l5 5-5 5" stroke="#fff" fill="none" stroke-width="1.6"/></svg>
    </a>
    <a class="scroll-down" href="#">
      <svg width="18" height="11" viewBox="0 0 18 11"><path d="M1 1l8 8 8-8" stroke="#1f2f5c" fill="none" stroke-width="2"/></svg>
    </a>
    <nav class="breadcrumb"><a href="#">Home</a>
      <svg width="9" height="8" viewBox="0 0 9 8"><path d="M1 1l3 3-3 3M5 1l3 3-3 3" stroke="#7d8bab" fill="none"/></svg>
      <span class="current">Blog</span></nav>
  </section>

  <h2 class="section-title">BLOG</h2>
  <div class="section-rule"></div>

  <main class="post-grid">
    <article class="post-card">
      <div class="post-media" role="img" aria-label="Person filling in an accident report on a clipboard beside a car" style="background:linear-gradient(135deg,#3c3f44,#9a9ea3 55%,#d6d7d8)"></div>
      <div class="post-body">
        <p class="post-meta"><span>Date:</span> 20 Nov 2025 - <em>Posted By Admin</em></p>
        <p class="post-meta"><span>Categories:</span> General Articles</p>
        <h3 class="post-title">What to Do Immediately After a Car Accident in Florida</h3>
        <p class="post-excerpt">On the other hand, we denounce with righteous indignation and dislike men who are so beguiled and by the charms of pleasure of the moment</p>
        <div class="post-actions"><a href="#">Read more <svg width="16" height="10" viewBox="0 0 16 10"><path d="M0 5h14M10 1l4 4-4 4" stroke="#1f2f5c" fill="none" stroke-width="1.3"/></svg></a><span class="sep"></span><a href="#"><svg width="14" height="14" viewBox="0 0 14 14" fill="none" stroke="#1f2f5c" stroke-width="1.2"><circle cx="11" cy="3" r="2"/><circle cx="3" cy="7" r="2"/><circle cx="11" cy="11" r="2"/><path d="M4.8 6l4.4-2M4.8 8l4.4 2"/></svg>Share It</a></div>
      </div>
    </article>
    <article class="post-card">
      <div class="post-media" role="img" aria-label="Client working on a laptop at home" style="background:linear-gradient(135deg,#e9e7e2,#c8cbd0 50%,#2b3550)"></div>
      <div class="post-body">
        <p class="post-meta"><span>Date:</span> 20 Nov 2025 - <em>Posted By Admin</em></p>
        <p class="post-meta"><span>Categories:</span> General Articles</p>
        <h3 class="post-title">How KestavLaw Helps You Without Office Visits</h3>
        <p class="post-excerpt">On the other hand, we denounce with righteous indignation and dislike men who are so beguiled and by the charms of pleasure of the moment</p>
        <div class="post-actions"><a href="#">Read more <svg width="16" height="10" viewBox="0 0 16 10"><path d="M0 5h14M10 1l4 4-4 4" stroke="#1f2f5c" fill="none" stroke-width="1.3"/></svg></a><span class="sep"></span><a href="#"><svg width="14" height="14" viewBox="0 0 14 14" fill="none" stroke="#1f2f5c" stroke-width="1.2"><circle cx="11" cy="3" r="2"/><circle cx="3" cy="7" r="2"/><circle cx="11" cy="11" r="2"/><path d="M4.8 6l4.4-2M4.8 8l4.4 2"/></svg>Share It</a></div>
      </div>
    </article>
    <article class="post-card">
      <div class="post-media" role="img" aria-label="Scales of justice and gavel on a wooden desk" style="background:linear-gradient(180deg,#2a2622,#7a5a3a 60%,#b88a5a)"></div>
      <div class="post-body">
        <p class="post-meta"><span>Date:</span> 20 Nov 2025 - <em>Posted By Admin</em></p>
        <p class="post-meta"><span>Categories:</span> General Articles</p>
        <h3 class="post-title">Top 5 Mistakes to Avoid After an Accident</h3>
        <p class="post-excerpt">On the other hand, we denounce with righteous indignation and dislike men who are so beguiled and by the charms of pleasure of the moment</p>
        <div class="post-actions"><a href="#">Read more <svg width="16" height="10" viewBox="0 0 16 10"><path d="M0 5h14M10 1l4 4-4 4" stroke="#1f2f5c" fill="none" stroke-width="1.3"/></svg></a><span class="sep"></span><a href="#"><svg width="14" height="14" viewBox="0 0 14 14" fill="none" stroke="#1f2f5c" stroke-width="1.2"><circle cx="11" cy="3" r="2"/><circle cx="3" cy="7" r="2"/><circle cx="11" cy="11" r="2"/><path d="M4.8 6l4.4-2M4.8 8l4.4 2"/></svg>Share It</a></div>
      </div>
    </article>
    <article class="post-card">
      <div class="post-media" role="img" aria-label="Handshake over documents on an office table" style="background:linear-gradient(135deg,#1e3140,#4f6574 50%,#d8d6d0)"></div>
      <div class="post-body">
        <p class="post-meta"><span>Date:</span> 20 Nov 2025 - <em>Posted By Admin</em></p>
        <p class="post-meta"><span>Categories:</span> General Articles</p>
        <h3 class="post-title">Lawyer After a Minor Accident? The Truth About Small Claims</h3>
        <p class="post-excerpt">On the other hand, we denounce with righteous indignation and dislike men who are so beguiled and by the charms of pleasure of the moment</p>
        <div class="post-actions"><a href="#">Read more <svg width="16" height="10" viewBox="0 0 16 10"><path d="M0 5h14M10 1l4 4-4 4" stroke="#1f2f5c" fill="none" stroke-width="1.3"/></svg></a><span class="sep"></span><a href="#"><svg width="14" height="14" viewBox="0 0 14 14" fill="none" stroke="#1f2f5c" stroke-width="1.2"><circle cx="11" cy="3" r="2"/><circle cx="3" cy="7" r="2"/><circle cx="11" cy="11" r="2"/><path d="M4.8 6l4.4-2M4.8 8l4.4 2"/></svg>Share It</a></div>
      </div>
    </article>
    <article class="post-card">
      <div class="post-media" role="img" aria-label="Lawyer in a suit at a desk with a gavel" style="background:linear-gradient(135deg,#1a2236,#3a4663 50%,#e6e6e6)"></div>
      <div class="post-body">
        <p class="post-meta"><span>Date:</span> 20 Nov 2025 - <em>Posted By Admin</em></p>
        <p class="post-meta"><span>Categories:</span> General Articles</p>
        <h3 class="post-title">What to Do Immediately After a Car Accident in Florida</h3>
        <p class="post-excerpt">On the other hand, we denounce with righteous indignation and dislike men who are so beguiled and by the charms of pleasure of the moment</p>
        <div class="post-actions"><a href="#">Read more <svg width="16" height="10" viewBox="0 0 16 10"><path d="M0 5h14M10 1l4 4-4 4" stroke="#1f2f5c" fill="none" stroke-width="1.3"/></svg></a><span class="sep"></span><a href="#"><svg width="14" height="14" viewBox="0 0 14 14" fill="none" stroke="#1f2f5c" stroke-width="1.2"><circle cx="11" cy="3" r="2"/><circle cx="3" cy="7" r="2"/><circle cx="11" cy="11" r="2"/><path d="M4.8 6l4.4-2M4.8 8l4.4 2"/></svg>Share It</a></div>
      </div>
    </article>
    <article class="post-card">
      <div class="post-media" role="img" aria-label="Scales, gavel and an open book on a lawyer's desk" style="background:linear-gradient(180deg,#e8e6e2,#9a8d7c 55%,#2a2826)"></div>
      <div class="post-body">
        <p class="post-meta"><span>Date:</span> 20 Nov 2025 - <em>Posted By Admin</em></p>
        <p class="post-meta"><span>Categories:</span> General Articles</p>
        <h3 class="post-title">How KestavLaw Helps You Without Office Visits</h3>
        <p class="post-excerpt">On the other hand, we denounce with righteous indignation and dislike men who are so beguiled and by the charms of pleasure of the moment</p>
        <div class="post-actions"><a href="#">Read more <svg width="16" height="10" viewBox="0 0 16 10"><path d="M0 5h14M10 1l4 4-4 4" stroke="#1f2f5c" fill="none" stroke-width="1.3"/></svg></a><span class="sep"></span><a href="#"><svg width="14" height="14" viewBox="0 0 14 14" fill="none" stroke="#1f2f5c" stroke-width="1.2"><circle cx="11" cy="3" r="2"/><circle cx="3" cy="7" r="2"/><circle cx="11" cy="11" r="2"/><path d="M4.8 6l4.4-2M4.8 8l4.4 2"/></svg>Share It</a></div>
      </div>
    </article>
    <article class="post-card">
      <div class="post-media" role="img" aria-label="Documents, envelope and gavel on a wooden table" style="background:linear-gradient(135deg,#5a3c22,#a87a48 50%,#d9c7a4)"></div>
      <div class="post-body">
        <p class="post-meta"><span>Date:</span> 20 Nov 2025 - <em>Posted By Admin</em></p>
        <p class="post-meta"><span>Categories:</span> General Articles</p>
        <h3 class="post-title">Top 5 Mistakes to Avoid After an Accident</h3>
        <p class="post-excerpt">On the other hand, we denounce with righteous indignation and dislike men who are so beguiled and by the charms of pleasure of the moment</p>
        <div class="post-actions"><a href="#">Read more <svg width="16" height="10" viewBox="0 0 16 10"><path d="M0 5h14M10 1l4 4-4 4" stroke="#1f2f5c" fill="none" stroke-width="1.3"/></svg></a><span class="sep"></span><a href="#"><svg width="14" height="14" viewBox="0 0 14 14" fill="none" stroke="#1f2f5c" stroke-width="1.2"><circle cx="11" cy="3" r="2"/><circle cx="3" cy="7" r="2"/><circle cx="11" cy="11" r="2"/><path d="M4.8 6l4.4-2M4.8 8l4.4 2"/></svg>Share It</a></div>
      </div>
    </article>
    <article class="post-card">
      <div class="post-media" role="img" aria-label="Insurance policy papers and a coffee cup on a table" style="background:linear-gradient(135deg,#7a5530,#e4ddd2 50%,#8a7f74)"></div>
      <div class="post-body">
        <p class="post-meta"><span>Date:</span> 20 Nov 2025 - <em>Posted By Admin</em></p>
        <p class="post-meta"><span>Categories:</span> General Articles</p>
        <h3 class="post-title">Lawyer After a Minor Accident? The Truth About Small Claims</h3>
        <p class="post-excerpt">On the other hand, we denounce with righteous indignation and dislike men who are so beguiled and by the charms of pleasure of the moment</p>
        <div class="post-actions"><a href="#">Read more <svg width="16" height="10" viewBox="0 0 16 10"><path d="M0 5h14M10 1l4 4-4 4" stroke="#1f2f5c" fill="none" stroke-width="1.3"/></svg></a><span class="sep"></span><a href="#"><svg width="14" height="14" viewBox="0 0 14 14" fill="none" stroke="#1f2f5c" stroke-width="1.2"><circle cx="11" cy="3" r="2"/><circle cx="3" cy="7" r="2"/><circle cx="11" cy="11" r="2"/><path d="M4.8 6l4.4-2M4.8 8l4.4 2"/></svg>Share It</a></div>
      </div>
    </article>
  </main>

  <aside class="sidebar">
    <div class="widget widget-search">
      <h3>Search</h3>
      <div class="search-field"><svg width="16" height="16" viewBox="0 0 16 16" fill="none" stroke="#5a6b93" stroke-width="1.4"><circle cx="7" cy="7" r="5.5"/><path d="M11 11l4 4"/></svg>Search here</div>
    </div>
    <div class="widget">
      <div class="widget-head">Categories</div>
      <ul class="cat-list">
        <li><svg width="18" height="16" viewBox="0 0 18 16" fill="none" stroke="#1f2f5c" stroke-width="1.6"><path d="M2 2l6 6-6 6M9 2l6 6-6 6"/></svg>General Articles</li>
        <li><svg width="18" height="16" viewBox="0 0 18 16" fill="none" stroke="#1f2f5c" stroke-width="1.6"><path d="M2 2l6 6-6 6M9 2l6 6-6 6"/></svg>Photos</li>
        <li><svg width="18" height="16" viewBox="0 0 18 16" fill="none" stroke="#1f2f5c" stroke-width="1.6"><path d="M2 2l6 6-6 6M9 2l6 6-6 6"/></svg>Videos</li>
      </ul>
    </div>
    <div class="widget">
      <div class="widget-head">Recent Posts</div>
      <ul class="recent-list">
        <li><div class="recent-thumb" role="img" aria-label="Professional reviewing papers at a desk" style="background:linear-gradient(135deg,#3a4b63,#b79a78)"></div><div><h4>Premises Explained</h4><p class="recent-date"><svg width="16" height="16" viewBox="0 0 16 16" fill="none" stroke="#c9a03b" stroke-width="1.3"><circle cx="8" cy="8" r="6.5"/><path d="M8 4v4l2.5 2"/></svg>20 Nov 2025</p></div></li>
        <li><div class="recent-thumb" role="img" aria-label="Signing a policy document" style="background:linear-gradient(135deg,#e8e3da,#9a7a56)"></div><div><h4>Remote Legal Help</h4><p class="recent-date"><svg width="16" height="16" viewBox="0 0 16 16" fill="none" stroke="#c9a03b" stroke-width="1.3"><circle cx="8" cy="8" r="6.5"/><path d="M8 4v4l2.5 2"/></svg>20 Nov 2025</p></div></li>
        <li><div class="recent-thumb" role="img" aria-label="Motorcycle crash on a road" style="background:linear-gradient(180deg,#5f7a4a,#8e9296)"></div><div><h4>Florida Accident Laws</h4><p class="recent-date"><svg width="16" height="16" viewBox="0 0 16 16" fill="none" stroke="#c9a03b" stroke-width="1.3"><circle cx="8" cy="8" r="6.5"/><path d="M8 4v4l2.5 2"/></svg>20 Nov 2025</p></div></li>
        <li><div class="recent-thumb" role="img" aria-label="Stressed driver reading papers" style="background:linear-gradient(135deg,#6d6f73,#d4d2ce)"></div><div><h4>Car Accident Tips</h4><p class="recent-date"><svg width="16" height="16" viewBox="0 0 16 16" fill="none" stroke="#c9a03b" stroke-width="1.3"><circle cx="8" cy="8" r="6.5"/><path d="M8 4v4l2.5 2"/></svg>20 Nov 2025</p></div></li>
        <li><div class="recent-thumb" role="img" aria-label="Damaged cars after a collision" style="background:linear-gradient(135deg,#3a3d40,#a3a6a8)"></div><div><h4>Insurance Claim Myths</h4><p class="recent-date"><svg width="16" height="16" viewBox="0 0 16 16" fill="none" stroke="#c9a03b" stroke-width="1.3"><circle cx="8" cy="8" r="6.5"/><path d="M8 4v4l2.5 2"/></svg>20 Nov 2025</p></div></li>
      </ul>
    </div>
  </aside>

  <nav class="pagination">
    <a class="page-num" href="#" style="left:0;gap:6px"><svg width="14" height="12" viewBox="0 0 14 12" fill="none" stroke="#6e6e6e" stroke-width="1.5"><path d="M7 1L2 6l5 5M12 1L7 6l5 5"/></svg>Previous</a>
    <a class="page-num is-current" href="#" style="left:112px">1</a>
    <a class="page-num" href="#" style="left:153px">2</a>
    <a class="page-num" href="#" style="left:179px">3</a>
    <span class="page-num" style="left:207px">....</span>
    <a class="page-num" href="#" style="left:238px">12</a>
    <a class="page-num" href="#" style="left:280px;gap:6px">Next<svg width="14" height="12" viewBox="0 0 14 12" fill="none" stroke="#6e6e6e" stroke-width="1.5"><path d="M2 1l5 5-5 5M7 1l5 5-5 5"/></svg></a>
  </nav>

  <footer class="site-footer">
    <svg class="footer-curve" width="1200" height="120" viewBox="0 0 1200 120">
      <path d="M0 0 H1200 V18 Q600 100 0 18 Z" fill="#ffffff"/>
      <path d="M0 28 Q600 110 1200 28" fill="none" stroke="#c9a03b" stroke-width="3"/>
    </svg>
    <div class="footer-brand">
      <div class="brand-mark"></div>
      <div class="brand-name">DELLACORTE LAW</div>
    </div>
    <div class="socials">
      <a class="on" href="#">Lumo</a><a href="#">Kip</a><a href="#">Nodd</a><a href="#">Pixo</a>
    </div>
    <div class="footer-col" style="left:414px">
      <h5>QUICK LINKS</h5><div class="rule"></div>
      <ul><li>Home</li><li>About Us</li><li>Services</li><li>Testimonials</li><li>FAQ’s</li><li>Contact Us</li><li>Make a Payment</li></ul>
    </div>
    <div class="footer-col" style="left:624px">
      <h5>SERVICES</h5><div class="rule"></div>
      <ul><li>Auto Accident</li><li>Negligence</li><li>Motorcycle Accident</li><li>Motorcycle Accident</li><li>Insurance Claims</li><li>Motorcycle Accident</li></ul>
    </div>
    <div class="footer-col" style="left:871px;width:260px">
      <h5>CONTACT DETAILS</h5><div class="rule"></div>
      <ul class="contact-list">
        <li><svg width="14" height="16" viewBox="0 0 14 16"><path fill="#c9a03b" d="M7 0a6 6 0 00-6 6c0 4.5 6 10 6 10s6-5.5 6-10a6 6 0 00-6-6zm0 8.5A2.5 2.5 0 117 3.5a2.5 2.5 0 010 5z"/></svg>123, Loream Ipsum Dollar Road, Florida. FL - 123 456</li>
        <li><svg width="14" height="14" viewBox="0 0 24 24"><path fill="#c9a03b" d="M6.6 10.8a15.1 15.1 0 006.6 6.6l2.2-2.2a1 1 0 011-.25 11.4 11.4 0 003.6.57 1 1 0 011 1V20a1 1 0 01-1 1A17 17 0 013 4a1 1 0 011-1h3.5a1 1 0 011 1c0 1.25.2 2.45.57 3.57a1 1 0 01-.25 1z"/></svg>(555) 123-4567</li>
        <li><svg width="15" height="12" viewBox="0 0 15 12"><rect width="15" height="12" rx="1" fill="#c9a03b"/><path d="M1 1.5l6.5 5 6.5-5" stroke="#050505" fill="none" stroke-width="1.2"/></svg>info@kestavlaw.example</li>
        <li><svg width="15" height="15" viewBox="0 0 16 16" fill="none" stroke="#c9a03b" stroke-width="1.5"><circle cx="8" cy="8" r="6.5"/><path d="M8 4v4l2.5 2"/></svg>Monday - Friday: 9:00 AM - 6:00 PM<br>Weekends: By appointment only</li>
      </ul>
    </div>
    <div class="footer-bottom"></div>
    <p class="copyright">© 2025 Dellacorte Law. All rights reserved. &nbsp;| &nbsp;<strong>Terms and Conditions</strong></p>
    <div class="pay-methods"><span>Crestpay</span><span>Novacard</span><span>Orbitcard</span><span>Walletry</span><span>Vantix</span></div>
  </footer>

</div>
</body>
</html>
```